Design needed for Cover of Conference Brochure

We are a conference company that puts on several business conferences per year. We are putting together a new conference - the Brightpath Insight Forum, and our audience is UX practitioners and specialists, product designers, UX designers, etc.
We need a brochure cover created. We are looking for fresh design ideas and are open to varying color schemes - please just keep in mind that this is a conference for business professionals, and fonts and colors should reflect this. Only restriction is that we do have a general cover format that we follow - i.e. which text goes where. (I've attached samples from our other events to reference.) We also generally have a central image to each brochure - feel free to submit a few versions with different images... we want something that accurately represents UX. However, if the design is compelling enough, image might not be completely necessary. We are relatively flexible - we just want something sharp!
- Must include KLVO logo (see placing on sample event covers)
- Must include footer - see sample covers
- Red text in word document are notes to you the designer - not actual text meant to appear on the cover
This cover is standard 8x11, and will be used for web only, not print. I have attached a word doc that includes all of the text that you will need for the cover. We will need final version in PDF, jpeg, and PSD. Please message me with any questions or clarification.

```html
<!DOCTYPE html>
<html lang="en">
<head>
<meta charset="utf-8">
<title>Brightpath Insight Forum — Brochure Cover</title>
<link rel="stylesheet" href="https://fonts.googleapis.com/css2?family=Quicksand:wght@400;500;700&display=swap">
<style>
  :root {
    --accent: #eeff1e;
    --ink: #1c1c1c;
    --bg-dark: #1f1f1f;
    --bg-mid: #3a3a3a;
    --panel: rgba(150,150,150,0.38);
    --rule: rgba(40,40,40,0.55);
    --white: #ffffff;
    --tile-blue: #2aa7e8;
  }
  * { margin: 0; padding: 0; box-sizing: border-box; }
  html, body { width: 873px; height: 1200px; overflow: hidden; background: var(--bg-dark); }
  body { font-family: "Quicksand", "Century Gothic", sans-serif; }

  .cover {
    position: relative; width: 873px; height: 1200px; overflow: hidden;
    background:
      linear-gradient(160deg, transparent 0 38%, rgba(255,255,255,0.05) 38% 55%, transparent 55%),
      linear-gradient(25deg, rgba(0,0,0,0.25) 0 30%, transparent 30%),
      radial-gradient(ellipse at 50% 40%, var(--bg-mid) 0%, var(--bg-dark) 75%);
  }

  .event-bar {
    position: absolute; left: 0; top: 0; width: 100%; height: 117px;
    background: var(--accent); color: var(--ink); text-align: center;
  }
  .event-date { font-size: 33px; font-weight: 700; padding-top: 14px; line-height: 1.2; }
  .event-venue { font-size: 22px; font-weight: 500; margin-top: 4px; }

  .organiser {
    position: absolute; left: 33px; top: 152px;
    display: flex; align-items: center; gap: 10px;
  }
  .organiser-mark { width: 22px; height: 22px; background: var(--tile-blue); border-radius: 4px; }
  .organiser-name { font-size: 26px; font-weight: 700; color: var(--white); }

  .title {
    position: absolute; left: 0; top: 180px; width: 100%; text-align: center;
  }
  .title-main {
    display: block; font-size: 150px; font-weight: 700; line-height: 200px;
    letter-spacing: -2px; color: var(--accent);
  }
  .title-sub {
    display: block; margin-top: 20px; font-size: 44px; font-weight: 500;
    line-height: 1.2; color: var(--accent);
  }
  .title-sub strong { font-weight: 700; }

  .title-rule {
    position: absolute; left: 38px; top: 466px; width: 798px; height: 2px; background: var(--accent);
  }

  .tagline {
    position: absolute; left: 0; top: 476px; width: 100%; text-align: center;
    color: var(--accent); font-size: 25px; font-weight: 500; line-height: 1.3;
  }
  .tagline strong { font-weight: 700; }

  .early-bird {
    position: absolute; left: 0; top: 578px; width: 100%; height: 46px;
    background: var(--accent); color: var(--ink);
    display: flex; align-items: center; justify-content: center;
    font-size: 26px; font-weight: 500; gap: 8px;
  }
  .early-bird strong { font-weight: 700; }
  .early-bird .saving {
    background: var(--ink); color: var(--accent); font-weight: 700; padding: 0 6px; line-height: 36px;
  }

  .new-label {
    position: absolute; left: 33px; top: 643px; width: 140px; height: 42px;
    background: rgba(70,70,70,0.85); color: var(--accent);
    font-size: 31px; font-weight: 700; padding-left: 14px; line-height: 42px;
  }

  .highlights {
    position: absolute; left: 33px; top: 685px; width: 807px; height: 350px;
    background: var(--panel); list-style: none; padding: 0 0 0 80px;
  }
  .highlight {
    display: flex; align-items: center; gap: 16px; height: 87px;
    border-bottom: 1px solid var(--rule);
    color: var(--accent); font-size: 27px; font-weight: 500; line-height: 1.22;
    margin-right: 52px;
  }
  .highlight:last-child { border-bottom: none; margin-right: 0; }
  .highlight strong { font-weight: 700; }
  .tick { flex: 0 0 54px; width: 54px; height: 44px; }

  .cta {
    position: absolute; left: 0; top: 1058px; width: 100%; text-align: center;
    color: var(--accent); font-size: 35px; font-weight: 500;
  }
  .cta strong { font-weight: 700; }

  .footer {
    position: absolute; left: 0; top: 1122px; width: 100%; height: 78px;
    background: var(--accent); color: var(--ink);
    display: flex; align-items: center; justify-content: center; gap: 14px;
    font-size: 28px; font-weight: 500;
  }
  .footer-item { display: flex; align-items: center; gap: 8px; }
  .footer-divider { width: 1px; height: 40px; background: var(--ink); margin: 0 6px; }
  .footer svg { width: 24px; height: 24px; }
</style>
</head>
<body>
<main class="cover">

  <header class="event-bar">
    <p class="event-date">June 10-12, 2014</p>
    <p class="event-venue">Harborline Assembly Hall &amp; Hotel, Oakridge, CA</p>
  </header>

  <div class="organiser">
    <span class="organiser-mark"></span>
    <span class="organiser-name">KLVO</span>
  </div>

  <h1 class="title">
    <span class="title-main">Brightpath</span>
    <span class="title-sub"><strong>Insight</strong> Forum</span>
  </h1>

  <div class="title-rule"></div>

  <p class="tagline">Design Compelling Experiences<br>through <strong>Successful UX Strategy</strong></p>

  <p class="early-bird">Register by <strong>March 7th, 2014</strong> and save <span class="saving">$400!</span></p>

  <p class="new-label">NEW:</p>

  <ul class="highlights">
    <li class="highlight">
      <svg class="tick" viewBox="0 0 54 44" aria-hidden="true"><rect x="2" y="10" width="32" height="32" fill="none" stroke="#eeff1e" stroke-width="4"/><path d="M9 24 L18 34 L48 4" fill="none" stroke="#eeff1e" stroke-width="7" stroke-linecap="round" stroke-linejoin="round"/></svg>
      <span>Case Studies from Leading Brands on<br>Executing an <strong>Effective UX Strategy</strong></span>
    </li>
    <li class="highlight">
      <svg class="tick" viewBox="0 0 54 44" aria-hidden="true"><rect x="2" y="10" width="32" height="32" fill="none" stroke="#eeff1e" stroke-width="4"/><path d="M9 24 L18 34 L48 4" fill="none" stroke="#eeff1e" stroke-width="7" stroke-linecap="round" stroke-linejoin="round"/></svg>
      <span>LearnHow UX-Driven Innovation<br><strong>Can Change Your Business</strong></span>
    </li>
    <li class="highlight">
      <svg class="tick" viewBox="0 0 54 44" aria-hidden="true"><rect x="2" y="10" width="32" height="32" fill="none" stroke="#eeff1e" stroke-width="4"/><path d="M9 24 L18 34 L48 4" fill="none" stroke="#eeff1e" stroke-width="7" stroke-linecap="round" stroke-linejoin="round"/></svg>
      <span>Build a Successful UX Team<br>that Operates <strong>Strategically</strong></span>
    </li>
    <li class="highlight">
      <svg class="tick" viewBox="0 0 54 44" aria-hidden="true"><rect x="2" y="10" width="32" height="32" fill="none" stroke="#eeff1e" stroke-width="4"/><path d="M9 24 L18 34 L48 4" fill="none" stroke="#eeff1e" stroke-width="7" stroke-linecap="round" stroke-linejoin="round"/></svg>
      <span>Insights into UX Research, User Behavior,<br>Usability Testing, Lean UX, <strong>and More</strong></span>
    </li>
  </ul>

  <p class="cta">▼ Register <strong>Today!</strong> ▼</p>

  <footer class="footer">
    <span class="footer-item">
      <svg viewBox="0 0 24 24" aria-hidden="true"><circle cx="12" cy="12" r="10" fill="none" stroke="#1c1c1c" stroke-width="2"/><ellipse cx="12" cy="12" rx="4.5" ry="10" fill="none" stroke="#1c1c1c" stroke-width="2"/><path d="M2 12 H22 M4 7 H20 M4 17 H20" stroke="#1c1c1c" stroke-width="1.6"/></svg>
      www.brightpathforum.com
    </span>
    <span class="footer-divider"></span>
    <span class="footer-item">
      <svg viewBox="0 0 24 24" aria-hidden="true"><rect x="1" y="1" width="22" height="22" rx="4" fill="#1c1c1c"/><path d="M8 5 L10.5 8.5 L9 10.5 C10 12.8 11.2 14 13.5 15 L15.5 13.5 L19 16 L17.5 19 C11 19 5 13 5 6.5 Z" fill="#eeff1e"/></svg>
      888.5550.0142
    </span>
  </footer>

</main>
</body>
</html>
```